Business card for a boutique travel agency VELARIEN

we need a business card design - double sided. We would like to have a very elegant, sophisticated but modern design. we are travel consultants and our business focus is Europe, mainly the city of Paris. We would like to receive designs in white and silver, black color but if you are confident that we should pick up a color to make it different and more beautful...go ahead! We are going to give business cards to our clients and business partners. It is important to be perceived as elegant, modern and trustful. Please check jpg references.

Target Market(s)

Velarien primary clients are individuals, couples and affinity groups of high-net-worth who travel for leisure at least once per year. Seeking the ultimate travel experience, the target clients demand the finest quality activities and accommodations accompanied by a superior level of service.

Industry/Entity Type

Travel Industry

Contact Information for Business Card

Lucinda Farrow
- lucinda@velarien-example.com
- +55 11 98347.2516
- velarien-example.com
- unique travel experiences (we would like to see this signature printed as a detail)

Font styles to use
Sans Serif

Colors

Designer to choose colors to be used in the design.

Requirements
Must have
• the Velarien logo that I have attached
Nice to have
• we would like to have some nice detail, something different that shows that we care about,... we are detail oriented.
Should not have
• decorative fonts

```html
<!DOCTYPE html>
<html lang="en">
<head>
<meta charset="utf-8">
<title>Velarien — Business Card</title>
<link rel="stylesheet" href="https://fonts.googleapis.com/css2?family=Roboto+Condensed:wght@300;400;700&display=swap">
<style>
  :root {
    --backdrop: #ebebeb;
    --card: #4a4a4b;
    --card-shade: #424243;
    --mark: #3b3b3c;
    --ink-light: #ffffff;
    --ink-soft: #dcdcdc;
  }
  * { margin: 0; padding: 0; box-sizing: border-box; }
  html, body {
    width: 1200px;
    height: 787px;
    overflow: hidden;
    background: var(--backdrop);
  }
  .stage {
    width: 1200px;
    height: 787px;
    display: flex;
    align-items: center;
    justify-content: center;
    gap: 60px;
  }
  .card {
    position: relative;
    width: 520px;
    height: 298px;
    background: linear-gradient(135deg, var(--card) 0%, var(--card-shade) 100%);
    overflow: hidden;
    box-shadow: 0 6px 18px rgba(0, 0, 0, 0.12);
    font-family: "Roboto Condensed", sans-serif;
  }

  /* Back side: centred name */
  .card--back {
    display: flex;
    align-items: center;
    justify-content: center;
    gap: 14px;
  }
  .back-dot {
    width: 14px;
    height: 14px;
    border-radius: 50%;
    background: var(--mark);
  }
  .back-name {
    font-weight: 300;
    font-size: 44px;
    letter-spacing: 0.12em;
    color: var(--mark);
  }

  /* Front side: oversized name and contact block */
  .front-name {
    position: absolute;
    left: -6px;
    top: 30px;
    white-space: nowrap;
    font-weight: 300;
    font-size: 86px;
    line-height: 1;
    letter-spacing: 0.14em;
    color: var(--mark);
  }
  .contact {
    position: absolute;
    left: 34px;
    bottom: 26px;
    color: var(--ink-soft);
    text-transform: uppercase;
  }
  .contact__name {
    font-weight: 700;
    font-size: 22px;
    line-height: 1;
    color: var(--ink-light);
    text-transform: none;
  }
  .contact__tagline {
    font-weight: 400;
    font-size: 9px;
    letter-spacing: 0.12em;
    margin-top: 5px;
  }
  .contact__phone {
    font-weight: 300;
    font-size: 9px;
    letter-spacing: 0.1em;
    margin-top: 20px;
  }
  .contact__lines {
    margin-top: 10px;
    display: flex;
    flex-direction: column;
    gap: 4px;
    font-weight: 300;
    font-size: 9px;
    letter-spacing: 0.1em;
  }
  .contact__row {
    display: flex;
    align-items: center;
    gap: 18px;
  }
  .contact__social {
    display: flex;
    align-items: center;
    gap: 5px;
  }
  .contact__bullet {
    width: 6px;
    height: 6px;
    background: var(--ink-soft);
  }
</style>
</head>
<body>
  <main class="stage">
    <section class="card card--back" aria-label="Card back">
      <span class="back-dot"></span>
      <span class="back-name">VELARIEN</span>
    </section>

    <section class="card card--front" aria-label="Card front">
      <div class="front-name">VELARIEN</div>
      <div class="contact">
        <p class="contact__name">Lucinda Farrow</p>
        <p class="contact__tagline">Unique travel experiences</p>
        <p class="contact__phone">+55 11 98347.2516</p>
        <div class="contact__lines">
          <div class="contact__row">
            <span>velarien-example.com</span>
            <span class="contact__social"><span class="contact__bullet"></span>Velarien</span>
          </div>
          <div class="contact__row">
            <span class="contact__social"><span class="contact__bullet"></span>Velarien</span>
          </div>
          <div class="contact__row">
            <span>lucinda@velarien-example.com</span>
          </div>
        </div>
      </div>
    </section>
  </main>
</body>
</html>
```